Super elegant, crisp & clean Business card design required

We recently upgraded our branding - which is on our website - tavorelstudio.com

I would like a simple, yet elegant, clean business card design please.

The font of my logo is Cinzel - and because of the natural colour - it's best to have this on a black background.

I would like to have the back of the business card - with simply my logo.

PLEASE DO NOT SUBMIT A COMPLICATED / UNCLEAN DESIGN

Industry/Entity Type

Business

Contact Information for Business Card

Dalvik Ostrander Photography

Font styles to use
Other font styles liked:
• Cinzel

Requirements
Must have
• A backpage with nothing but my logo
• Simple design - stands out
Should not have
• Colour that dont align with my logo
• Over complicated '/ non symmetrical design

```html
<!DOCTYPE html>
<html lang="en">
<head>
<meta charset="utf-8">
<title>Dalvik Ostrander Photography – Business Card</title>
<link href="https://fonts.googleapis.com/css2?family=Cinzel:wght@400;500&family=Open+Sans:wght@400&display=swap" rel="stylesheet">
<style>
  :root {
    --backdrop: #d9d9d7;
    --taupe: #857660;
    --taupe-dark: #75674f;
    --paper: #ffffff;
    --ink-light: #f4efe6;
    --shadow: rgba(0, 0, 0, 0.22);
  }
  * { box-sizing: border-box; margin: 0; padding: 0; }
  html, body {
    width: 1200px;
    height: 696px;
    overflow: hidden;
    background: var(--backdrop);
  }
  .canvas {
    position: relative;
    width: 1200px;
    height: 696px;
  }
  .card {
    position: absolute;
    top: 205px;
    width: 500px;
    height: 286px;
    box-shadow: 0 6px 18px var(--shadow);
    overflow: hidden;
  }
  .card--back {
    left: 70px;
    background: var(--taupe);
    display: flex;
    flex-direction: column;
    align-items: center;
    justify-content: center;
  }
  .card--front {
    left: 630px;
    background: var(--paper);
  }
  .card__diagonal {
    position: absolute;
    inset: 0;
  }
  .brand {
    text-align: center;
    font-family: "Cinzel", serif;
  }
  .brand__mark {
    width: 14px;
    height: 14px;
    border-radius: 50%;
    margin: 0 auto 16px;
  }
  .brand__name {
    font-size: 21px;
    font-weight: 400;
    letter-spacing: 1px;
    line-height: 1;
  }
  .brand__tagline {
    margin-top: 4px;
    font-size: 9px;
    letter-spacing: 7px;
    line-height: 1;
  }
  .card--back .brand { color: var(--ink-light); }
  .card--back .brand__mark { background: var(--ink-light); }
  .card--front .brand {
    position: absolute;
    top: 70px;
    right: 34px;
    color: var(--taupe);
  }
  .card--front .brand__mark { background: var(--taupe); }
  .contact {
    position: absolute;
    left: 28px;
    bottom: 26px;
    list-style: none;
    font-family: "Open Sans", sans-serif;
    font-size: 12.5px;
    line-height: 1.6;
    color: var(--paper);
  }
</style>
</head>
<body>
  <main class="canvas">
    <section class="card card--back" aria-label="Card back">
      <div class="brand">
        <div class="brand__mark"></div>
        <p class="brand__name">Dalvik Ostrander</p>
        <p class="brand__tagline">PHOTOGRAPHY</p>
      </div>
    </section>

    <section class="card card--front" aria-label="Card front">
      <svg class="card__diagonal" viewBox="0 0 500 286" preserveAspectRatio="none" aria-hidden="true">
        <polygon points="0,0 105,0 430,286 0,286" fill="var(--taupe)"/>
      </svg>
      <div class="brand">
        <div class="brand__mark"></div>
        <p class="brand__name">Dalvik Ostrander</p>
        <p class="brand__tagline">PHOTOGRAPHY</p>
      </div>
      <ul class="contact">
        <li>T : +63 917 555 0142</li>
        <li>W : www.tavorelstudio.com</li>
        <li>E : info@tavorelstudio.com</li>
      </ul>
    </section>
  </main>
</body>
</html>
```